Vel Framewright - Worpress Design

We are a consultancy to help builders to optimize their planning in order to save building costs. For that reason we need a website to offer our services, present our history, the mission and offer a plug-in for a first contact (including calendar), testimonials, a blog etc.
As an idea, I really like: https://www.kestrumadvisory.de/
Later on the website should be programmed in www.wolkanet.de in our Wordpress area. The text, of course, will be done by myself. The colors should be suitable to our recently designed logo.

```html
<!DOCTYPE html>
<html lang="en">
<head>
<meta charset="utf-8">
<title>Vel Framewright – Consulting</title>
<link href="https://fonts.googleapis.com/css2?family=Orbitron:wght@700;800;900&family=Poppins:wght@400;500;600;700&display=swap" rel="stylesheet">
<style>
:root{
  --gold:#d9a441;
  --gold-light:#efc65f;
  --gold-dark:#b57c22;
  --ink:#232428;
  --dark:#2b2d33;
  --text:#4a4a4a;
  --white:#ffffff;
  --soft:#f1ece2;
}
*{margin:0;padding:0;box-sizing:border-box}
html,body{width:1200px;height:4468px;overflow:hidden;background:var(--white)}
body{position:relative;font-family:'Poppins',sans-serif;color:var(--text)}
.abs{position:absolute}
.display{font-family:'Orbitron',sans-serif;font-weight:800;text-transform:uppercase;color:var(--ink);letter-spacing:1px;white-space:nowrap}
.btn{position:absolute;display:flex;align-items:center;justify-content:center;color:#fff;font-weight:600;font-size:15px;letter-spacing:.5px;text-transform:uppercase;background:linear-gradient(90deg,var(--gold-dark),var(--gold-light));clip-path:polygon(0 0,100% 0,88% 100%,0 100%);padding-right:14px}
.photo{position:absolute}
.deco{position:absolute}

/* header */
.site-header{position:absolute;left:88px;top:14px;width:1022px;height:73px;background:#fff;box-shadow:0 4px 20px rgba(0,0,0,.15)}
.brand{position:absolute;left:18px;top:20px;display:flex;align-items:center;gap:10px;font-weight:700;font-size:22px;color:var(--gold);white-space:nowrap}
.brand-mark{width:22px;height:22px;background:var(--gold)}
.topbar{position:absolute;left:351px;top:0;right:0;height:28px;background:linear-gradient(90deg,var(--gold-dark),var(--gold-light));clip-path:polygon(4% 0,100% 0,100% 100%,0 100%);display:flex;align-items:center;gap:22px;padding-left:36px;color:#fff;font-size:11px;white-space:nowrap}
.topbar .soc{display:flex;gap:8px}
.topbar .soc i{width:9px;height:9px;border-radius:50%;background:#fff;display:block}
.nav{position:absolute;right:22px;top:45px;display:flex;gap:30px;font-size:13px;color:var(--ink);align-items:center}

/* hero */
.hero-title{color:#fff;font-size:68px;line-height:1}
.hero-sub{left:340px;width:520px;top:470px;text-align:center;color:#fff;font-size:17px;line-height:27px}

/* about */
.about-text{left:631px;top:1090px;width:440px;font-size:13.5px;line-height:22px}

/* services */
.service{position:absolute;top:1604px;width:245px}
.service-icon{width:92px;height:78px;background:var(--dark);clip-path:polygon(0 0,100% 0,70% 100%,0 100%);display:flex;align-items:center;padding-left:20px}
.service-icon.gold{background:var(--gold)}
.service h3{font-family:'Orbitron',sans-serif;font-weight:800;font-size:15px;color:var(--ink);margin-top:24px;text-transform:uppercase;white-space:nowrap}
.service p{font-size:13px;line-height:20px;margin-top:10px}

/* blog */
.card{position:absolute;top:2771px;width:288px;height:402px;background:#fff;box-shadow:0 20px 40px rgba(0,0,0,.12);clip-path:polygon(0 0,100% 0,100% 92%,0 100%)}
.card .photo{left:0;top:0;width:288px;height:241px}
.card h4{position:absolute;left:30px;top:272px;font-family:'Orbitron',sans-serif;font-weight:800;font-size:15px;color:var(--ink)}
.card p{position:absolute;left:30px;top:298px;width:235px;font-size:12.5px;line-height:20px}
.card .more{position:absolute;left:30px;top:364px;font-size:11px;font-weight:700;color:var(--gold-dark)}
.card .more b{color:var(--gold-light)}

/* contact */
.field{position:absolute;left:700px;width:327px;height:44px;background:#fff;font-size:14px;color:#333;padding:13px 24px}

/* footer */
.foot-col{position:absolute;top:4130px;font-size:12.5px;color:#fff;line-height:23px}
.foot-col h5{font-family:'Orbitron',sans-serif;font-weight:800;font-size:15px;color:var(--gold);margin-bottom:4px;text-transform:uppercase}
</style>
</head>
<body>

<!-- HERO -->
<div class="photo" role="img" aria-label="Photo of business people in hard hats shaking hands at a construction site" style="left:0;top:0;width:1200px;height:860px;background:linear-gradient(135deg,#4b4f57 0%,#353840 45%,#24262b 100%);clip-path:polygon(0 0,1200px 0,1200px 760px,0 860px)"></div>
<svg class="abs" style="left:0;top:0" width="1200" height="880">
  <defs><linearGradient id="g1" x1="0" x2="1"><stop offset="0" stop-color="#c68f2f"/><stop offset="1" stop-color="#efc65f"/></linearGradient></defs>
  <polygon points="700,770 1200,700 1200,858 1100,858" fill="url(#g1)"/>
</svg>

<header class="site-header">
  <div class="brand"><span class="brand-mark"></span>Vel Framewright</div>
  <div class="topbar">
    <span>Some oes address here</span><span>kontakt@velframewright.de</span>
    <span class="soc"><i></i><i></i><i></i><i></i></span>
    <span>Request a free initial consultation</span>
  </div>
  <nav class="nav">
    <svg width="12" height="12"><path d="M6 1 L11 6 H9 V11 H3 V6 H1Z" fill="#d9a441"/></svg>
    <span>About Us</span><span>Offers</span><span>Testimonials</span><span>Blog</span><span>Press</span><span>Contact</span>
    <svg width="12" height="12"><circle cx="5" cy="5" r="4" fill="none" stroke="#232428" stroke-width="1.6"/><path d="M8 8 L11 11" stroke="#232428" stroke-width="1.6"/></svg>
  </nav>
</header>

<div class="abs display hero-title" style="top:322px;left:240px">Rethinking</div>
<div class="abs display hero-title" style="top:396px;left:600px">Advice</div>
<div class="abs hero-sub">Vel Framewright Consulting helps you get more clients and make your service company digital.</div>

<div class="deco" role="img" aria-label="Decorative gold ornament" style="left:0;top:680px;width:170px;height:340px;border-radius:0 170px 170px 0;background:radial-gradient(circle at 0 50%,rgba(217,164,65,.25),rgba(217,164,65,0) 70%)"></div>
<svg class="abs" style="left:590px;top:808px" width="20" height="92">
  <g fill="#d9a441"><path d="M3 2h14l-7 8z"/><path d="M3 20h14l-7 8z"/><path d="M3 38h14l-7 8z"/><path d="M3 56h14l-7 8z"/><path d="M3 74h14l-7 8z"/></g>
</svg>

<!-- ABOUT -->
<div class="deco" role="img" aria-label="Decorative silver and gold building outline" style="left:120px;top:925px;width:450px;height:455px;background:linear-gradient(90deg,#ececec 0%,#f4f4f4 50%,var(--soft) 100%)"></div>
<div class="photo" role="img" aria-label="Photo of colleagues reviewing documents on a staircase" style="left:150px;top:1188px;width:173px;height:190px;background:linear-gradient(160deg,#d6d6d6,#6d6d6d)"></div>
<div class="photo" role="img" aria-label="Photo of an engineer in a white hard hat" style="left:404px;top:1065px;width:132px;height:313px;background:linear-gradient(160deg,#bfc4cc,#3c4150)"></div>

<div class="abs display" style="left:631px;top:1000px;font-size:34px;color:var(--gold)">About</div>
<div class="abs display" style="left:631px;top:1040px;font-size:32px">Vel Framewright</div>
<p class="abs about-text">We are a team of experts in construction planning and management. We have over 10 years of experience in helping builders achieve their goals and deliver quality projects on time and on budget. We use cutting-edge technology and innovative methods to optimize every aspect of the building process, from design to execution. Whether you need advice, guidance, or support, we are here to help you succeed. Contact us today and let us show you how we can make your vision a reality.</p>
<div class="btn" style="left:631px;top:1292px;width:160px;height:52px">Read More</div>

<!-- SERVICES -->
<div class="abs display" style="left:0;width:1200px;text-align:center;top:1502px;font-size:38px">Our Services</div>
<div class="service" style="left:88px">
  <div class="service-icon"><svg width="36" height="36" fill="none" stroke="#fff" stroke-width="1.6"><circle cx="18" cy="9" r="5"/><circle cx="8" cy="22" r="4"/><circle cx="28" cy="22" r="4"/><path d="M2 34v-4h12v4M22 34v-4h12v4"/></svg></div>
  <h3>Consultancy</h3><p>Lorem Ipsum has been the industry's standard dummy text ever since the 1500s, when an unknown printer took a galley of type .</p>
</div>
<div class="service" style="left:343px">
  <div class="service-icon gold"><svg width="36" height="36" fill="none" stroke="#fff" stroke-width="1.6"><path d="M9 14a9 9 0 0 1 18 0z"/><circle cx="18" cy="20" r="5"/><path d="M6 35c0-7 5-10 12-10s12 3 12 10"/></svg></div>
  <h3>Help Builders</h3><p>Lorem Ipsum has been the industry's standard dummy text ever since the 1500s, when an unknown printer took a galley of type .</p>
</div>
<div class="service" style="left:605px">
  <div class="service-icon"><svg width="36" height="36" fill="none" stroke="#fff" stroke-width="1.6"><rect x="5" y="5" width="20" height="28"/><path d="M10 13h10M10 19h10M10 25h6"/><circle cx="28" cy="26" r="5"/></svg></div>
  <h3>Planning in Order</h3><p>Lorem Ipsum has been the industry's standard dummy text ever since the 1500s, when an unknown printer took a galley of type .</p>
</div>
<div class="service" style="left:867px">
  <div class="service-icon"><svg width="36" height="36" fill="none" stroke="#fff" stroke-width="1.6"><circle cx="11" cy="11" r="7"/><path d="M20 33V22l8-6 7 6v11z"/><path d="M4 26c3 4 8 6 12 5"/></svg></div>
  <h3>Save Building Costs</h3><p>Lorem Ipsum has been the industry's standard dummy text ever since the 1500s, when an unknown printer took a galley of type .</p>
</div>

<!-- TRUST BAND -->
<div class="photo" role="img" aria-label="Photo of a smiling team meeting around a table" style="left:0;top:1925px;width:1200px;height:702px;background:linear-gradient(120deg,#3a3d45 0%,#5b5a58 50%,#2f3138 100%);clip-path:polygon(0 0,1200px 78px,1200px 555px,0 702px)"></div>
<svg class="abs" style="left:590px;top:1952px" width="20" height="100"><g fill="#d9a441"><path d="M3 2h14l-7 8z"/><path d="M3 22h14l-7 8z"/><path d="M3 42h14l-7 8z"/><path d="M3 62h14l-7 8z"/><path d="M3 82h14l-7 8z"/></g></svg>
<div class="abs display" style="left:0;width:1200px;text-align:center;top:2177px;font-size:46px;line-height:58px;color:#fff">Over <span style="color:var(--gold-light)">4,000</span> Customers<br>Already Trust Us.</div>
<p class="abs" style="left:300px;width:600px;top:2300px;text-align:center;color:#fff;font-size:17px;line-height:26px">A thriving business is not rocket science. Find out what experiences our customers have had.</p>
<div class="btn" style="left:452px;top:2369px;width:295px;height:55px">Customer Testimonials</div>

<!-- BLOG -->
<div class="abs display" style="left:0;width:1200px;text-align:center;top:2685px;font-size:38px">Latest Blog</div>
<article class="card" style="left:130px"><div class="photo" role="img" aria-label="Photo of hands arranging hexagon tiles on a wooden table" style="background:linear-gradient(150deg,#8a5c36,#c9a07a)"></div><h4>BLOG HEADING HERE</h4><p>Lorem Ipsum has been the industry's standard dummy text ever since the 1500s, when an unknown.</p><span class="more">READ <b>MORE</b></span></article>
<article class="card" style="left:458px"><div class="photo" role="img" aria-label="Photo of colleagues looking at a tablet in an office" style="background:linear-gradient(150deg,#9aa0a6,#3e4147)"></div><h4>BLOG HEADING HERE</h4><p>Lorem Ipsum has been the industry's standard dummy text ever since the 1500s, when an unknown.</p><span class="more">READ <b>MORE</b></span></article>
<article class="card" style="left:784px"><div class="photo" role="img" aria-label="Photo of business team discussing in a bright office" style="background:linear-gradient(150deg,#c4ccd6,#3a4150)"></div><h4>BLOG HEADING HERE</h4><p>Lorem Ipsum has been the industry's standard dummy text ever since the 1500s, when an unknown.</p><span class="more">READ <b>MORE</b></span></article>

<!-- CONSULTATION + CONTACT -->
<div class="abs display" style="left:109px;top:3430px;font-size:33px;line-height:40px">Book your free<br>performance<br>consultation now</div>
<p class="abs" style="left:109px;top:3564px;width:450px;font-size:13.5px;line-height:22px">Lorem Ipsum is simply dummy text of the printing and typesetting industry. Lorem Ipsum has been the industry's standard dummy text ever since the 1500s, when an unknown printer took a galley of type and scrambled it to make a type specimen book.</p>
<div class="btn" style="left:113px;top:3670px;width:280px;height:52px">Free Consultation Now</div>

<div class="abs" style="left:645px;top:3212px;width:438px;height:641px;background:linear-gradient(135deg,#b97f24 0%,#d9a441 50%,#efc65f 100%);clip-path:polygon(0 90px,438px 0,438px 560px,0 641px)"></div>
<div class="abs display" style="left:698px;top:3345px;font-size:34px;color:#fff">Contact Us</div>
<div class="field" style="top:3407px">Name</div>
<div class="field" style="top:3461px">Email</div>
<div class="field" style="top:3516px">Phone</div>
<div class="field" style="top:3569px">Select Date
  <svg class="abs" style="right:20px;top:14px" width="16" height="16" fill="none" stroke="#666"><rect x="1" y="2" width="14" height="13"/><path d="M1 6h14M5 9h2M9 9h2M5 12h2M9 12h2"/></svg></div>
<div class="field" style="top:3621px;height:168px">Message</div>
<svg class="abs" style="left:700px;top:3798px" width="60" height="62"><polygon points="0,0 60,30 0,62" fill="#232428"/><path d="M14 32 L32 24 L26 40 L23 33Z" fill="#fff"/></svg>

<!-- FOOTER -->
<svg class="abs" style="left:0;top:3905px" width="1200" height="563">
  <defs><linearGradient id="g3" x1="0" x2="1"><stop offset="0" stop-color="#c68f2f"/><stop offset="1" stop-color="#efc65f"/></linearGradient></defs>
  <rect x="0" y="0" width="1200" height="563" fill="#2a2b30"/>
  <polygon points="0,0 1200,0 1200,60 640,150" fill="#fff"/>
  <polygon points="640,150 1200,60 1200,115" fill="url(#g3)"/>
  <line x1="88" y1="505" x2="1110" y2="505" stroke="#44464d" stroke-width="1"/>
</svg>
<div class="brand abs" style="left:92px;top:4208px;font-size:22px"><span class="brand-mark"></span>Vel Framewright</div>
<div class="foot-col" style="left:404px"><h5>Useful Links</h5>Home<br>About Us<br>Offers<br>Testimonials<br>Blog<br>Press<br>Contact</div>
<div class="foot-col" style="left:633px"><h5>Our Services</h5>Consultancy<br>Help builders<br>planning in order<br>Save building costs</div>
<div class="foot-col" style="left:886px"><h5>Contact Us</h5>
  <span style="color:var(--gold)">●</span>&nbsp; Some goes address here<br>
  <span style="color:var(--gold)">●</span>&nbsp; info@velframewright.de<br>
  <span style="color:var(--gold)">●</span>&nbsp; +49 30 5550 1842<br>
  <span style="display:inline-flex;gap:14px;margin-top:10px"><i style="width:10px;height:10px;border-radius:50%;background:#fff;display:block"></i><i style="width:10px;height:10px;border-radius:50%;background:#fff;display:block"></i><i style="width:10px;height:10px;border-radius:50%;background:#fff;display:block"></i><i style="width:10px;height:10px;border-radius:50%;background:#fff;display:block"></i></span>
</div>
<div class="abs" style="left:0;width:1200px;text-align:center;top:4431px;color:#fff;font-size:13px">©Copyright 2023 | All Rights Reserved</div>
<svg class="abs" style="left:1118px;top:4384px" width="52" height="52"><circle cx="26" cy="26" r="26" fill="#d9a441"/><path d="M15 17h22v14H24l-6 5v-5h-3z" fill="#fff"/></svg>

</body>
</html>
```